Complete web design based around only our company logo

I need someone to build a web page based around our company logo. I will provide other sites that we like and would want our site to be similar to.
Updates

Please look at these websites to get an idea of our industry

larkspur minerals
tov minerals
granite royalty
windmere energy
harlow energy

Our company buys mineral rights, and royalties from mineral owners all over the united states.  We also lease minerals as well. 

What we are trying to have designed is a fully functioning website that you upload to our webhost after we approve of final design.  

Target Market(s)

Oil and Gas/Mineral Owners

Industry/Entity Type

It Company

Font styles to use
Serif
Sans Serif

Colors
9ccb3b

Requirements
Must have
• Quick Contact form

```html
<!DOCTYPE html>
<html lang="en">
<head>
<meta charset="utf-8">
<title>Eastbrook Resources</title>
<link href="https://fonts.googleapis.com/css2?family=Roboto:wght@400;500;700&family=Oswald:wght@600&display=swap" rel="stylesheet">
<style>
:root{
  --green:#3a7f08;
  --green-dark:#2f6e05;
  --green-text:#3b7d0c;
  --ink:#111;
  --body:#333;
  --muted:#666;
  --panel:#efefef;
  --panel-head:#5f5f5f;
  --field-border:#d9d9d9;
  --footer:#000;
}
*{box-sizing:border-box;margin:0;padding:0}
html,body{width:909px;height:1200px;overflow:hidden;background:#fff}
body{position:relative;font-family:"Roboto",Arial,sans-serif;color:var(--body)}
.header{position:absolute;left:0;top:0;width:909px;height:72px}
.brand{position:absolute;left:90px;top:16px;display:flex;align-items:center;gap:8px}
.brand-mark{width:30px;height:30px;border-radius:50%;background:var(--green)}
.brand-name{font-size:14px;font-weight:700;color:var(--green);line-height:1;text-transform:uppercase;letter-spacing:.5px}
.inquiry{position:absolute;right:91px;top:24px;text-align:right}
.inquiry small{display:block;font-size:9px;color:var(--ink);font-weight:500}
.inquiry strong{display:block;font-size:19px;color:var(--green);font-weight:700;line-height:1.05}
.band{position:absolute;left:0;top:72px;width:909px;height:298px;background:linear-gradient(var(--green) 0,var(--green) 30px,var(--green-dark) 31px,var(--green) 298px)}
.nav{position:absolute;left:90px;top:72px;width:730px;height:32px;display:flex;justify-content:space-between;align-items:center;padding:0 14px 0 14px}
.nav a{color:#fff;font-size:11.5px;text-decoration:none}
.hero{position:absolute;left:89px;top:104px;width:731px;height:294px;background:#fff;padding:4px;box-shadow:0 6px 8px -6px rgba(0,0,0,.35)}
.hero-photo{width:100%;height:100%;background:linear-gradient(100deg,#b9bcbd 0%,#c93a2a 30%,#9a9ea0 45%,#c99a3a 65%,#e0b23e 80%,#8e8a82 100%)}
.welcome{position:absolute;left:90px;top:436px;width:410px}
.welcome h1{font-size:21px;font-weight:500;color:var(--ink);margin-bottom:10px}
.welcome h1 span{color:var(--green-text);font-weight:400}
.welcome p{font-size:10.6px;line-height:12.8px;margin-bottom:13px;color:#222}
.feature{position:absolute;top:606px;width:205px}
.feature h2{font-family:"Oswald",Impact,sans-serif;font-size:20px;color:var(--ink);letter-spacing:-.5px;line-height:1;padding-bottom:3px;border-bottom:3px solid var(--green);width:200px;margin-bottom:8px}
.feature p{font-size:10.6px;line-height:12.8px;color:#222}
.testimonial{position:absolute;left:92px;width:452px}
.avatar{position:absolute;left:0;top:0;width:36px;height:48px;border:1px solid #ccc;padding:2px;background:#fff}
.avatar div{width:100%;height:100%;background:linear-gradient(#8a7868,#4a3f38)}
.quote{position:absolute;left:52px;top:0;width:400px;background:var(--panel);border:1px solid #d6d6d6;padding:11px 10px;font-size:8.3px;line-height:11.2px;color:#666}
.quote::before{content:"";position:absolute;left:-7px;top:14px;border:5px solid transparent;border-right-color:#d6d6d6;border-left:0}
.person{position:absolute;left:52px}
.person b{display:block;font-size:10.5px;color:var(--green-text)}
.person span{font-size:8.5px;color:var(--muted)}
.contact-panel{position:absolute;left:566px;top:439px;width:253px;height:511px;background:var(--panel)}
.contact-panel header{background:var(--panel-head);color:#fff;font-size:10.8px;line-height:13.5px;padding:9px 18px;height:44px}
.form{padding:12px 13px 0 13px}
.field{display:block;height:24px;border:1px solid var(--field-border);background:#fff;font-size:8.3px;color:#444;padding:6px 11px;margin-bottom:6.4px}
.row{display:flex;gap:2px}
.row .field{flex:1}
.status{font-size:8.3px;color:#555;margin:7px 3px 5px}
.radios{display:flex;gap:8px;font-size:8.3px;color:#999;margin:0 3px 9px}
.radios span{display:flex;align-items:center;gap:4px}
.radios i{width:10px;height:10px;border:1px solid #ccc;border-radius:50%;background:#fff}
.message{height:141px}
.submit{display:flex;align-items:center;gap:12px;width:114px;height:29px;background:#6b6b6b;color:#fff;font-size:11px;padding-left:9px;margin-top:14px}
.footer{position:absolute;left:0;top:978px;width:909px;height:222px;background:var(--footer);color:#fff}
.footer-brand{position:absolute;left:90px;top:26px}
.footer-brand .mark{width:46px;height:46px;border-radius:50%;background:#fff;margin-left:28px;margin-bottom:10px}
.footer-brand .name{font-size:15px;font-weight:700;text-transform:uppercase;letter-spacing:.5px}
.footer-brand p{font-size:8.2px;line-height:11px;margin-top:10px;width:180px}
.footer h3{font-family:"Oswald",Impact,sans-serif;font-size:17px;font-weight:600;letter-spacing:-.3px}
.footer-nav{position:absolute;left:365px;top:25px}
.footer-nav .cols{display:flex;gap:28px;margin-top:21px}
.footer-nav ul{list-style:none;font-size:10.5px;line-height:13.6px;width:76px}
.footer-contact{position:absolute;left:650px;top:25px}
.footer-contact b{display:block;font-size:10.6px;margin-top:21px}
.footer-contact address{font-style:normal;font-size:8.4px;line-height:13.6px;margin-top:3px}
.phone{display:flex;align-items:center;gap:5px;font-size:19px;font-weight:300;margin-top:5px;font-stretch:condensed;letter-spacing:-.5px}
.email{font-size:10.5px;margin-top:4px}
.footer-bottom{position:absolute;left:90px;top:186px;width:725px;border-top:1px solid #333;padding-top:9px;display:flex;justify-content:space-between;align-items:center}
.footer-bottom small{font-size:7.4px}
.social{display:flex;gap:5px;margin-top:-4px}
.social i{width:19px;height:19px;border-radius:50%;background:#9a9a9a}
</style>
</head>
<body>
<header class="header">
  <div class="brand"><div class="brand-mark"></div><div class="brand-name">Eastbrook<br>Resources</div></div>
  <div class="inquiry"><small>For Inquires Contact Us</small><strong>888-555-0147</strong></div>
</header>
<div class="band"></div>
<nav class="nav">
  <a>Home</a><a>About us</a><a>Active states</a><a>Lease/Purchase minerals</a><a>Testimonials</a><a>Careers</a><a>Contact us</a>
</nav>
<div class="hero"><div class="hero-photo" role="img" aria-label="Engineer in a hard hat and red jacket reviewing notes beside a yellow mining machine"></div></div>

<section class="welcome">
  <h1>Welcome to <span>Eastbrook Resources, LLC</span></h1>
  <p>Lorem ipsum dolor sit amet, consectetuer adipiscing elit, sed diam nonummy nibh euismod tincidunt ut laoreet dolore magna aliquam erat volutpat. Ut wisi enim ad minim veniam, quis nostrud exerci tation ullamcorper suscipit lobortis nisl ut aliquip ex ea commodo consequat.</p>
  <p>Duis autem vel eum iriure dolor in hendrerit in vulputate velit esse molestie consequat, vel illum dolore eu feugiat nulla facilisis at vero eros et accumsan et iusto odio dignissim qui blandit praesent luptatum zzril delenit augue duis dolore te feugait nulla facilisi.</p>
</section>

<section class="feature" style="left:90px">
  <h2>WHAT WE DO</h2>
  <p>Lorem ipsum dolor sit amet, consectetuer adipiscing elit, sed diam nonummy nibh euismod tincidunt ut laoreet dolore magna aliquam erat volutpat. Ut wisi enim ad minim veniam, quis nostrud exerci tation ullamcorper suscipit lobortis nisl ut aliquip ex ea commodo consequat.</p>
</section>
<section class="feature" style="left:337px">
  <h2>HOW WE DO IT</h2>
  <p>Duis autem vel eum iriure dolor in hendrerit in vulputate velit esse molestie consequat, vel illum dolore eu feugiat nulla facilisis at vero eros et accumsan et iusto odio dignissim qui blandit praesent luptatum zzril delenit augue duis dolore te feugait ulla facilisi.</p>
</section>

<div class="testimonial" style="top:758px">
  <div class="avatar"><div role="img" aria-label="Portrait of a client"></div></div>
  <blockquote class="quote">Ut enim ad minim veniam, quis nostrud exercitation ullamco laboris nisi ut aliquip ex ea commodo consequat. Duis aute irure dolor in reprehenderit in voluptate velit esse cillum praesent luptatum zzril delenit augue duis dolore te feugait ulla facilisi.</blockquote>
  <div class="person" style="top:64px"><b>Ravi Ostrander</b><span>Real Estate Guru</span></div>
</div>
<div class="testimonial" style="top:866px">
  <div class="avatar"><div role="img" aria-label="Portrait of a client"></div></div>
  <blockquote class="quote">Ut enim ad minim veniam, quis nostrud exercitation ullamco laboris nisi ut aliquip ex ea commodo consequat. Duis aute irure dolor in reprehenderit in voluptate velit esse cillum praesent luptatum zzril delenit augue duis dolore te feugait ulla facilisi.</blockquote>
  <div class="person" style="top:64px"><b>Lena Corvell</b><span>Expert Miner</span></div>
</div>

<aside class="contact-panel">
  <header>Contact Tov today for details about a lease or purchase offering for your property</header>
  <div class="form">
    <span class="field">Name *</span>
    <span class="field">Address *</span>
    <div class="row"><span class="field">Country *</span><span class="field">State *</span></div>
    <div class="row"><span class="field">City *</span><span class="field">Zip *</span></div>
    <span class="field">Phone *</span>
    <span class="field">Email *</span>
    <span class="field">Total Acres *</span>
    <div class="status">Current status of mineral rights</div>
    <div class="radios"><span><i></i>for sale</span><span><i></i>for lease</span></div>
    <span class="field message">Message *</span>
    <div class="submit">
      <svg width="19" height="19" viewBox="0 0 20 20"><circle cx="10" cy="10" r="10" fill="#fff"/><path d="M5 10h9M10 6l4 4-4 4" stroke="#6b6b6b" stroke-width="2.2" fill="none"/></svg>
      SUBMIT
    </div>
  </div>
</aside>

<footer class="footer">
  <div class="footer-brand">
    <div class="mark"></div>
    <div class="name">Eastbrook Resources</div>
    <p>Lorem ipsum dolor sit amet, consectetuer adipiscing elit, sed diam nonummy nibh euismod tincidunt ut laoreet dolore magna aliquam erat volutpat.</p>
  </div>
  <div class="footer-nav">
    <h3>NAVIGATION</h3>
    <div class="cols">
      <ul><li>Home</li><li>About us</li><li>Active states</li><li>Lease/purchase minerals</li></ul>
      <ul><li>Careers</li><li>Contact us</li><li>Terms of Use</li><li>Privacy Policy</li></ul>
    </div>
  </div>
  <div class="footer-contact">
    <h3>CONTACT US</h3>
    <b>Eastbrook Resources</b>
    <address>4410 Alder Ridge Road Suite 12<br>Millbrook, Ohio 440127</address>
    <div class="phone">
      <svg width="20" height="20" viewBox="0 0 20 20"><circle cx="10" cy="10" r="9" stroke="#fff" stroke-width="1.3" fill="none"/><path d="M7 5.5l1.6 2.4-1 1.1c.7 1.4 1.6 2.3 3 3l1.1-1 2.4 1.6-1 1.6c-3.5-.4-6.3-3.2-6.7-6.7z" fill="#fff"/></svg>
      0-12-5550198
    </div>
    <div class="email">info@eastbrookresources.com</div>
  </div>
  <div class="footer-bottom">
    <small>© Copyright 2014 Eastbrook Resources. All Rights Reserved</small>
    <div class="social"><i></i><i></i><i></i><i></i></div>
  </div>
</footer>
</body>
</html>
```